Buisness card

**Front Side:**

**[Your Company Logo]**
**Steadfast Upkeep Industrial**
*Keeping Your Equipment Running Smoothly*

**Contact Information:**
- **Name:** [darren Whitlow
- **Title:** [owner
- **Phone:** [8025196047
- **Email:** darren@sukrn.com

**Back Side:**

**Services Offered:**
- Routine Inspections
- Equipment Maintenance
- Emergency Repairs
- Consultation Services
- New installs
Tag line
Be proactive not reactive

```html
<!DOCTYPE html>
<html lang="en">
<head>
<meta charset="utf-8">
<title>Steadfast Upkeep Industrial – Business Card</title>
<link href="https://fonts.googleapis.com/css2?family=Montserrat:wght@400;500;600;700&display=swap" rel="stylesheet">
<style>
  :root {
    --navy: #253a7c;
    --sky: #27b3ee;
    --ink: #111111;
    --grey: #3a3a3a;
    --paper: #ffffff;
    --backdrop: #e9eaec;
  }
  * { box-sizing: border-box; margin: 0; padding: 0; }
  html, body { width: 1200px; height: 900px; overflow: hidden; }
  body {
    background: var(--backdrop);
    font-family: "Montserrat", sans-serif;
    position: relative;
  }
  .card {
    position: absolute;
    left: 250px;
    width: 700px;
    height: 400px;
    background: var(--paper);
    border-radius: 28px;
    box-shadow: 0 6px 18px rgba(0,0,0,0.12);
    overflow: hidden;
  }
  .card--front { top: 30px; }
  .card--back { top: 470px; }

  /* Logo side */
  .brand-block {
    position: absolute;
    left: 70px; top: 120px;
    display: flex; align-items: center; gap: 26px;
  }
  .brand-dot {
    width: 120px; height: 120px; border-radius: 50%;
    background: var(--navy); flex: none;
  }
  .brand-name {
    color: var(--navy);
    font-weight: 700;
    font-size: 34px;
    line-height: 1.1;
  }
  .brand-tagline {
    margin-top: 12px;
    color: var(--ink);
    font-weight: 600;
    font-size: 22px;
    letter-spacing: 0.5px;
    text-transform: uppercase;
  }

  /* Info side */
  .mini-brand {
    position: absolute; left: 40px; top: 40px;
    display: flex; align-items: center; gap: 12px;
  }
  .mini-dot { width: 46px; height: 46px; border-radius: 50%; background: var(--navy); flex: none; }
  .mini-name { color: var(--navy); font-weight: 700; font-size: 16px; line-height: 1.15; }
  .mini-tagline { color: var(--ink); font-weight: 600; font-size: 10px; text-transform: uppercase; margin-top: 3px; }

  .divider {
    position: absolute; left: 392px; top: 40px;
    width: 2px; height: 165px; background: var(--sky);
  }
  .person { position: absolute; left: 414px; top: 48px; right: 24px; }
  .person-name {
    color: var(--sky); font-weight: 700; font-size: 28px;
    line-height: 1.1; white-space: nowrap;
  }
  .person-title { color: var(--grey); font-size: 17px; margin-top: 4px; }
  .contact { margin-top: 16px; list-style: none; }
  .contact li {
    display: flex; align-items: center; gap: 8px;
    color: var(--grey); font-size: 17px; margin-bottom: 8px;
    white-space: nowrap;
  }
  .contact svg { width: 14px; height: 14px; fill: var(--sky); flex: none; }

  .services { position: absolute; left: 40px; right: 40px; top: 228px; }
  .services-heading { color: var(--sky); font-weight: 700; font-size: 22px; margin-bottom: 14px; }
  .services-list {
    list-style: none;
    display: grid; grid-template-columns: 180px 220px 200px;
    column-gap: 10px;
    row-gap: 14px;
  }
  .services-list li {
    display: flex; align-items: center; gap: 8px;
    color: var(--grey); font-size: 15px; white-space: nowrap;
  }
  .services-list li::before {
    content: ""; width: 11px; height: 11px; border-radius: 50%;
    background: var(--navy); flex: none;
  }
  .services-list .service--repairs { grid-column: 2; grid-row: 2; }
  .services-list .service--installs { grid-column: 3; grid-row: 2; }
</style>
</head>
<body>
  <section class="card card--front">
    <div class="brand-block">
      <div class="brand-dot"></div>
      <div>
        <div class="brand-name">Steadfast Upkeep<br>Industrial</div>
        <div class="brand-tagline">Be proactive not reactive</div>
      </div>
    </div>
  </section>

  <section class="card card--back">
    <div class="mini-brand">
      <div class="mini-dot"></div>
      <div>
        <div class="mini-name">Steadfast Upkeep Industrial</div>
        <div class="mini-tagline">Be proactive not reactive</div>
      </div>
    </div>

    <div class="divider"></div>

    <div class="person">
      <div class="person-name">darren Whitlow</div>
      <div class="person-title">Owner</div>
      <ul class="contact">
        <li>
          <svg viewBox="0 0 24 24"><path d="M6.6 10.8a15.1 15.1 0 0 0 6.6 6.6l2.2-2.2a1 1 0 0 1 1-.25 11.4 11.4 0 0 0 3.6.57 1 1 0 0 1 1 1V20a1 1 0 0 1-1 1A17 17 0 0 1 3 4a1 1 0 0 1 1-1h3.5a1 1 0 0 1 1 1c0 1.25.2 2.45.57 3.57a1 1 0 0 1-.25 1z"/></svg>
          8025196047
        </li>
        <li>
          <svg viewBox="0 0 24 24"><path d="M2 5h20v14H2z M2 5l10 8 10-8" stroke="#fff" stroke-width="1.5"/></svg>
          darren@sukrn.com
        </li>
      </ul>
    </div>

    <div class="services">
      <div class="services-heading">Services Offered</div>
      <ul class="services-list">
        <li>Routine Inspections</li>
        <li>Equipment Maintenance</li>
        <li>Consultation Services</li>
        <li class="service--repairs">Emergency Repairs</li>
        <li class="service--installs">New installs</li>
      </ul>
    </div>
  </section>
</body>
</html>
```